Rapidly growing regional logistics company looking for a modern clean website design.

We need a website for a 5 year old company based in New England.
We offer a complete logistics solution. With services dedicated to the changing economic environment. Services to our customers include, same day delivery, trucking and van service, warehouse & storage, pool distribution, and B2B installations.
We've implemented leading technology along the way, that provides visibility, accountability, up to the minute tracking, and project management.
Our goal to be known in the industry we service as an excellent provider of time-critical services and dependability.
Independently of the services we offer, our customers know that they can count on a true partner.

Target Market(s)

B2B, including printers, retail, manufacturers, wholesalers, electronics, any company that needs product delivered or warehoused

Industry/Entity Type

Logistics

Coding

Coded - Design and coding required

Number of Pages Required

5+ page

Font styles to use
Sans Serif

Colors
0255a3

Requirements
Must have
• Clean, modern design, limited clutter. Limited tabs, preferred everything on 1st screen roll down to see info

```html
<!DOCTYPE html>
<html lang="en">
<head>
<meta charset="utf-8">
<title>Harbor Logistics</title>
<link href="https://fonts.googleapis.com/css2?family=Raleway:wght@400;500;600;700&family=Lato:wght@400;700&display=swap" rel="stylesheet">
<style>
:root{
  --brand:#0255a3;
  --brand-dark:#01427f;
  --ink:#222428;
  --text:#6b6e73;
  --dark:#2f3033;
  --darker:#1b1c1e;
  --light:#f0f1f4;
  --light2:#e8eaed;
  --white:#ffffff;
  --line:#d6d9de;
}
*{box-sizing:border-box;margin:0;padding:0}
html,body{width:1200px;height:3000px;overflow:hidden}
body{position:relative;background:var(--white);font-family:'Lato',Arial,sans-serif;color:var(--text)}
.abs{position:absolute}
.heading{font-family:'Raleway',Arial,sans-serif;font-weight:500;color:var(--ink);font-size:27px;text-align:center;width:1200px;left:0}
.heading b{color:var(--brand);font-weight:500;text-transform:uppercase}
.divider{position:absolute;left:420px;width:360px;height:16px}
.divider::before,.divider::after{content:"";position:absolute;top:7px;width:160px;height:1px;background:var(--brand)}
.divider::before{left:0}.divider::after{right:0}
.divider span{position:absolute;left:172px;top:0;width:16px;height:16px;border-radius:50%;background:var(--brand)}
.divider.light::before,.divider.light::after{background:rgba(255,255,255,.7)}
.divider.light span{background:var(--white)}
.badge{position:absolute;left:568px;width:64px;height:64px;border-radius:50%;background:var(--white);border:4px solid var(--brand)}
.badge span{position:absolute;left:12px;top:12px;width:32px;height:32px;border-radius:50%;background:var(--brand)}

/* header */
.header{left:0;top:0;width:1200px;height:112px;background:var(--white)}
.logo{left:140px;top:8px;width:120px;text-align:center}
.logo-mark{width:58px;height:58px;border-radius:50%;background:var(--brand);margin:0 auto 2px}
.logo-name{font-family:'Raleway',Arial,sans-serif;font-weight:600;color:var(--brand);font-size:20px;line-height:18px;letter-spacing:1px}
.logo-name small{display:block;font-size:13px;letter-spacing:2px;font-weight:600}
.topbar{left:536px;top:0;width:664px;height:62px;background:linear-gradient(90deg,#2b2c2f,#0c0c0d)}
.topbar::before{content:"";position:absolute;left:-1px;top:0;border-top:62px solid var(--white);border-right:56px solid transparent}
.contact-item{top:12px;color:var(--white);font-size:13px;line-height:15px}
.contact-item b{display:block;font-weight:700;font-size:13px}
.contact-item .ico{position:absolute;left:-36px;top:2px;width:28px;height:28px;border:2px solid var(--white);border-radius:50%}
.nav{left:620px;top:86px;display:flex;gap:0}
.nav a{font-family:'Lato',Arial,sans-serif;text-decoration:none;color:var(--brand);font-size:14px;font-weight:700;margin-right:46px;position:relative;padding-bottom:10px}
.nav a.active::after{content:"";position:absolute;left:-4px;right:-4px;bottom:-2px;height:3px;background:var(--brand)}

/* hero */
.hero{left:0;top:112px;width:1200px;height:516px;background:linear-gradient(180deg,#c9dcee 0%,#eef3f2 30%,#b8c79a 52%,#6f8f4a 72%,#8d8a80 100%)}
.hero-arrow{top:254px;width:40px;height:40px;border:3px solid var(--white);border-radius:50%}
.hero-arrow svg{position:absolute;left:9px;top:9px}
.hero-caption{left:0;top:450px;width:1200px;height:66px;background:rgba(35,30,25,.72);color:var(--white);font-family:'Raleway',Arial,sans-serif;font-weight:600;font-size:21px;line-height:26px;text-align:center;padding-top:8px;text-transform:uppercase}

/* welcome */
.welcome-text{left:160px;top:732px;width:880px;text-align:center;font-size:13.5px;line-height:23px;color:#7a7d82}
.btn-more{left:534px;top:822px;width:128px;height:38px;background:#3a3b3d;color:var(--white);font-size:14px;font-family:'Lato',Arial,sans-serif;line-height:38px;padding-left:14px}
.btn-more i{position:absolute;right:-8px;top:5px;width:28px;height:28px;border-radius:50%;background:var(--brand);border:2px solid var(--white)}
.btn-more i svg{position:absolute;left:7px;top:6px}

/* services */
.services{left:0;top:920px;width:1200px;height:500px;background:linear-gradient(135deg,#2c6fb4 0%,#1f5fa5 45%,#4a83bf 70%,#2a68ad 100%)}
.services .heading{color:var(--white)}
.services .heading b{color:var(--white)}
.card{top:166px;width:198px;height:286px;background:var(--white);box-shadow:0 2px 6px rgba(0,0,0,.25)}
.card-title{position:absolute;left:16px;top:-4px;width:166px;height:38px;background:#3b3c3e;color:var(--white);font-size:13px;text-align:center;text-transform:uppercase;line-height:14px;display:flex;align-items:center;justify-content:center}
.card-img{position:absolute;left:8px;top:46px;width:182px;height:128px}
.card-text{position:absolute;left:12px;top:182px;width:174px;text-align:center;font-size:11.5px;line-height:16px;color:#555}
.card-btn{position:absolute;left:50px;top:250px;width:98px;height:24px;border-radius:12px;background:var(--brand);color:var(--white);font-size:12px;text-align:center;line-height:24px;font-weight:700}

/* why */
.why{left:0;top:1420px;width:1200px;height:614px;background:var(--light)}
.feature{left:188px;width:560px;height:110px;border-bottom:1px solid var(--line)}
.feature .ico{position:absolute;left:0;top:0;width:62px;height:62px;background:var(--brand);border-radius:4px}
.feature .ico svg{position:absolute;left:13px;top:13px}
.feature h3{position:absolute;left:82px;top:4px;font-family:'Raleway',Arial,sans-serif;font-weight:600;font-size:18px;color:var(--ink)}
.feature p{position:absolute;left:82px;top:32px;width:460px;font-size:12px;line-height:18px;color:#666}
.person{left:780px;top:140px;width:290px;height:474px;background:linear-gradient(180deg,#e3e5e9 0%,#cfd2d8 40%,#3c3f46 60%,#24262b 100%);border-radius:140px 140px 0 0}

/* testimonials */
.quote-box{left:208px;top:2148px;width:784px;height:110px;border:1px solid var(--line);background:var(--white)}
.quote-box::after{content:"";position:absolute;left:88px;bottom:-11px;width:20px;height:20px;background:var(--white);border-right:1px solid var(--line);border-bottom:1px solid var(--line);transform:rotate(45deg)}
.quote-text{position:absolute;left:70px;top:24px;width:650px;text-align:center;font-size:11.5px;line-height:18px;color:#555}
.qmark{position:absolute;font-family:Georgia,serif;font-size:46px;color:#c8cbd0;line-height:1}
.quote-name{left:330px;top:2266px;font-size:12px;font-weight:700;color:var(--brand)}
.ring-arrow{width:26px;height:26px;border:2px solid #c6c9ce;border-radius:50%}
.ring-arrow svg{position:absolute;left:6px;top:5px}

/* clients */
.clients{left:0;top:2340px;width:1200px;height:270px;background:var(--light2)}
.client{top:122px;width:146px;height:72px;background:var(--white);display:flex;align-items:center;justify-content:center;gap:8px;font-family:'Lato',Arial,sans-serif;font-weight:700;font-size:20px;color:#444;box-shadow:0 1px 3px rgba(0,0,0,.12)}
.client i{width:14px;height:14px;border-radius:50%;background:#444;display:block}

/* footer */
.footer{left:0;top:2610px;width:1200px;height:342px;background:linear-gradient(180deg,#3a3b3e 0%,#26272a 100%)}
.footer h4{position:absolute;top:94px;font-family:'Lato',Arial,sans-serif;color:var(--white);font-size:14px;font-weight:700}
.quick{position:absolute;left:142px;top:128px;list-style:none}
.quick li{color:var(--white);font-size:12px;line-height:21.5px;padding-left:14px;position:relative}
.quick li::before{content:"";position:absolute;left:0;top:7px;border-left:6px solid var(--white);border-top:4px solid transparent;border-bottom:4px solid transparent}
.field{position:absolute;left:362px;width:240px;height:22px;background:#4a4b4e;border:1px solid #5b5c60;color:#aaa;font-size:10px;padding:4px 8px}
.send{position:absolute;left:362px;top:268px;width:78px;height:24px;background:var(--brand);color:var(--white);font-size:13px;font-weight:700;text-align:center;line-height:24px}
.c-line{position:absolute;left:722px;color:var(--white);font-size:11px;line-height:16px;padding-left:18px}
.c-line svg{position:absolute;left:0;top:2px}
.social{position:absolute;left:958px;color:var(--white);font-size:11px;font-weight:700;line-height:24px;padding-left:34px}
.social i{position:absolute;left:0;top:0;width:24px;height:24px;border-radius:50%;display:block}
.copyright{left:0;top:2952px;width:1200px;height:48px;background:var(--brand);color:var(--white);font-size:12px;text-align:center;line-height:48px}
</style>
</head>
<body>

<header class="header abs">
  <div class="logo abs">
    <div class="logo-mark"></div>
    <div class="logo-name">HARBOR<small>LOGISTICS</small></div>
  </div>
  <div class="topbar abs">
    <div class="contact-item abs" style="left:92px">
      <span class="ico"><svg width="24" height="24" viewBox="0 0 24 24"><path d="M8 6l2 3-1.5 1.5c.8 1.8 2.2 3.2 4 4L14 13l3 2-1 2.5c-4.5 0-9-4.5-9-9z" fill="#fff"/></svg></span>
      <b>CALL US:</b>555.201.4480
    </div>
    <div class="contact-item abs" style="left:264px">
      <span class="ico"><svg width="24" height="24" viewBox="0 0 24 24"><path d="M12 5a4 4 0 0 0-4 4c0 3 4 8 4 8s4-5 4-8a4 4 0 0 0-4-4zm0 5.5a1.5 1.5 0 1 1 0-3 1.5 1.5 0 0 1 0 3z" fill="#fff"/></svg></span>
      <b>LOCATION:</b>118 Wharf Street Ste 4, Newport Falls, RI 02899
    </div>
  </div>
  <nav class="nav abs">
    <a class="active" href="#">HOME</a><a href="#">ABOUT US</a><a href="#">SERVICES</a><a href="#">CONTACT US</a>
  </nav>
</header>

<section class="hero abs" role="img" aria-label="Photo of a delivery truck driving on a country road through green hills at sunrise">
  <span class="hero-arrow abs" style="left:100px"><svg width="16" height="16" viewBox="0 0 16 16"><path d="M11 2L5 8l6 6" stroke="#fff" stroke-width="3" fill="none"/></svg></span>
  <span class="hero-arrow abs" style="left:1058px;opacity:.6"><svg width="16" height="16" viewBox="0 0 16 16"><path d="M5 2l6 6-6 6" stroke="#fff" stroke-width="3" fill="none"/></svg></span>
  <div class="hero-caption abs">We offer a complete logistics solution with services<br>dedicated to the changing economic environment</div>
</section>

<section class="welcome">
  <h1 class="heading abs" style="top:662px">Welcome to <b>Harbor Logistics</b></h1>
  <div class="divider" style="top:698px"><span></span></div>
  <p class="welcome-text abs">Our company was founded in 2012 but our team is seasoned, with a combined 75 years of experience.<br>Harbor Logistics offers a complete logistics solution. With services dedicated to the changing economic environment. Services to our customers include, same day delivery, trucking and van service, warehouse &amp; storage, pool distribution, and B2B white glove &amp; installations.</p>
  <div class="btn-more abs">READ MORE<i><svg width="12" height="14" viewBox="0 0 12 14"><path d="M3 2l5 5-5 5" stroke="#fff" stroke-width="2.5" fill="none"/></svg></i></div>
</section>

<section class="services abs">
  <div class="badge" style="top:10px"><span></span></div>
  <h2 class="heading abs" style="top:76px">Our <b>Services</b></h2>
  <div class="divider light" style="top:112px"><span></span></div>

  <article class="card abs" style="left:158px">
    <div class="card-title">Same Day Delivery</div>
    <div class="card-img" role="img" aria-label="Photo of a courier handing a parcel to a customer at a door" style="background:linear-gradient(135deg,#e9e4dc,#b79f86 60%,#5b4a3d)"></div>
    <p class="card-text">Regardless of the specifics of your needs, HARBOR can handle your same-day delivery needs...</p>
    <div class="card-btn">Read More</div>
  </article>
  <article class="card abs" style="left:386px">
    <div class="card-title">Trucking and Van<br>Service</div>
    <div class="card-img" role="img" aria-label="Photo of yellow trucks parked at a depot under a blue sky" style="background:linear-gradient(180deg,#6fa0d4 0%,#a9c6e4 45%,#d9b63a 60%,#7a7d80 100%)"></div>
    <p class="card-text">Rush and pre-scheduled delivery Light and heavy trucking (cargo vans to liftgates)...</p>
    <div class="card-btn">Read More</div>
  </article>
  <article class="card abs" style="left:614px">
    <div class="card-title">Warehouse &amp; Storage</div>
    <div class="card-img" role="img" aria-label="Photo of a long warehouse aisle lined with tall storage racks" style="background:linear-gradient(90deg,#8a6b4a,#d9d4cc 45%,#e6e2da 55%,#7c6246)"></div>
    <p class="card-text">Our warehouse facility may prove to be one of the most valuable extensions of your company's...</p>
    <div class="card-btn">Read More</div>
  </article>
  <article class="card abs" style="left:842px">
    <div class="card-title">Pool Distribution</div>
    <div class="card-img" role="img" aria-label="Photo of workers in safety vests checking goods in a distribution center" style="background:linear-gradient(135deg,#c9b58c,#d8a24a 50%,#6b6f6a)"></div>
    <p class="card-text">Pool Distribution is the distribution of product to numerous customers within a particular geographic...</p>
    <div class="card-btn">Read More</div>
  </article>
</section>

<section class="why abs">
  <h2 class="heading abs" style="top:54px">Why <b>Choose Us</b></h2>
  <div class="divider" style="top:90px"><span></span></div>

  <div class="feature abs" style="top:144px">
    <div class="ico"><svg width="36" height="36" viewBox="0 0 36 36"><path d="M2 18s6-10 16-10 16 10 16 10-6 10-16 10S2 18 2 18z" fill="#fff"/><circle cx="18" cy="18" r="6" fill="#0255a3"/><circle cx="18" cy="18" r="2.5" fill="#fff"/></svg></div>
    <h3>Visibility</h3>
    <p>Lorem ipsum dolouar sit amet consec tetuer adipiscing elnit. Praebulum molesbeutie lacus. Aenea nonuendrerit maurihasellu porta wiorhjowerjowerew.</p>
  </div>
  <div class="feature abs" style="top:260px">
    <div class="ico"><svg width="36" height="36" viewBox="0 0 36 36"><rect x="7" y="5" width="22" height="28" rx="2" fill="none" stroke="#fff" stroke-width="2.5"/><rect x="13" y="2" width="10" height="6" rx="1" fill="#fff"/><path d="M11 14h14M11 19h14M11 24h8" stroke="#fff" stroke-width="2"/><circle cx="26" cy="27" r="6" fill="#fff"/><path d="M23 27l2 2 4-4" stroke="#0255a3" stroke-width="2" fill="none"/></svg></div>
    <h3>Accountability</h3>
    <p>Lorem ipsum dolouar sit amet consec tetuer adipiscing elnit. Praebulum molesbeutie lacus. Aenea nonuendrerit maurihasellu porta wiorhjowerjowerew.</p>
  </div>
  <div class="feature abs" style="top:376px">
    <div class="ico"><svg width="36" height="36" viewBox="0 0 36 36"><path d="M3 30l8-16 8 8 6-4 8 12z" fill="none" stroke="#fff" stroke-width="2"/><path d="M18 3a7 7 0 0 0-7 7c0 5 7 12 7 12s7-7 7-12a7 7 0 0 0-7-7z" fill="#fff"/><circle cx="18" cy="10" r="2.5" fill="#0255a3"/></svg></div>
    <h3>Up to the Minute Tracking</h3>
    <p>Lorem ipsum dolouar sit amet consec tetuer adipiscing elnit. Praebulum molesbeutie lacus. Aenea nonuendrerit maurihasellu porta wiorhjowerjowerew.</p>
  </div>
  <div class="feature abs" style="top:494px;border-bottom:none">
    <div class="ico"><svg width="36" height="36" viewBox="0 0 36 36"><rect x="5" y="5" width="22" height="28" rx="2" fill="none" stroke="#fff" stroke-width="2.5"/><path d="M9 12h14M9 17h10" stroke="#fff" stroke-width="2"/><circle cx="25" cy="25" r="8" fill="#fff"/><path d="M25 20v5l3 2" stroke="#0255a3" stroke-width="2" fill="none"/></svg></div>
    <h3>Project Management.</h3>
    <p>Lorem ipsum dolouar sit amet consec tetuer adipiscing elnit. Praebulum molesbeutie lacus. Aenea nonuendrerit maurihasellu porta wiorhjowerjowerew.</p>
  </div>

  <div class="person abs" role="img" aria-label="Photo of a businesswoman in a dark suit holding a clipboard"></div>
</section>

<section class="testimonials">
  <h2 class="heading abs" style="top:2066px">Client <b>Testimonials</b></h2>
  <div class="divider" style="top:2102px"><span></span></div>
  <span class="ring-arrow abs" style="left:140px;top:2190px"><svg width="12" height="14" viewBox="0 0 12 14"><path d="M8 2L3 7l5 5" stroke="#c6c9ce" stroke-width="2" fill="none"/></svg></span>
  <span class="ring-arrow abs" style="left:1032px;top:2190px"><svg width="12" height="14" viewBox="0 0 12 14"><path d="M4 2l5 5-5 5" stroke="#c6c9ce" stroke-width="2" fill="none"/></svg></span>
  <div class="quote-box abs">
    <span class="qmark" style="left:36px;top:14px">&ldquo;</span>
    <p class="quote-text">Lorem ipsum dolor sitamet, consectetuer adipiscing sed diam nonummy nibh euismod tincidunt ut laoreet dolore magna aliqua volutpat. Ut wisi enim ad minim veniam, quis nostrud exerci tation ullamcorper suscipit lobortis nisl ut aliquip ex ea commodo consequat. Duis autem vel eum iriure dolor in hendrerit in vulputate velit esse molestie consequat.</p>
    <span class="qmark" style="left:630px;top:78px">&rdquo;</span>
  </div>
  <div class="quote-name abs">Mr. Arlen Voss</div>
</section>

<section class="clients abs">
  <h2 class="heading abs" style="top:40px">Our <b>Clients</b></h2>
  <div class="divider" style="top:76px"><span></span></div>
  <span class="ring-arrow abs" style="left:140px;top:144px"><svg width="12" height="14" viewBox="0 0 12 14"><path d="M8 2L3 7l5 5" stroke="#c6c9ce" stroke-width="2" fill="none"/></svg></span>
  <span class="ring-arrow abs" style="left:1032px;top:144px"><svg width="12" height="14" viewBox="0 0 12 14"><path d="M4 2l5 5-5 5" stroke="#c6c9ce" stroke-width="2" fill="none"/></svg></span>
  <div class="client abs" style="left:194px">Norvale</div>
  <div class="client abs" style="left:364px"><i></i>Brightway</div>
  <div class="client abs" style="left:528px">Tallow</div>
  <div class="client abs" style="left:692px"><i></i>Quarrin</div>
  <div class="client abs" style="left:860px">Pelham</div>
</section>

<footer class="footer abs">
  <div class="badge" style="top:-24px"><span></span></div>

  <h4 style="left:142px">Quick Links</h4>
  <ul class="quick">
    <li>Home</li><li>About Us</li><li>Services</li><li>News</li><li>Clients</li><li>Contact Us</li>
  </ul>

  <h4 style="left:362px">Quick Enquiry</h4>
  <div class="field" style="top:126px">Name</div>
  <div class="field" style="top:152px">Email</div>
  <div class="field" style="top:178px">Subject</div>
  <div class="field" style="top:204px;height:60px">Message</div>
  <div class="send">SEND</div>

  <h4 style="left:722px">Contact Us</h4>
  <div class="c-line" style="top:124px"><svg width="10" height="12" viewBox="0 0 10 12"><path d="M5 0a4 4 0 0 0-4 4c0 3 4 8 4 8s4-5 4-8a4 4 0 0 0-4-4z" fill="#fff"/></svg><b>HARBOR LOGISTICS</b><br>118 Wharf Street Ste 4<br>Newport Falls, RI 02899</div>
  <div class="c-line" style="top:182px"><svg width="10" height="12" viewBox="0 0 10 12"><path d="M2 1l2 3-1 1c.5 1.5 1.5 2.5 3 3l1-1 3 2-1 2C4 11 0 7 0 2z" fill="#fff"/></svg>555.201.4480</div>
  <div class="c-line" style="top:212px"><svg width="10" height="12" viewBox="0 0 10 12"><rect x="0" y="3" width="10" height="6" fill="#fff"/><rect x="2" y="0" width="6" height="3" fill="#fff"/></svg>555.201.4480</div>
  <div class="c-line" style="top:242px"><svg width="10" height="12" viewBox="0 0 10 12"><rect x="0" y="3" width="10" height="7" fill="#fff"/><path d="M0 3l5 4 5-4" stroke="#333" fill="none"/></svg>hello@harborlogistics.example</div>

  <h4 style="left:958px">Follow Us</h4>
  <div class="social" style="top:120px"><i style="background:#3b5998"></i>Social Page</div>
  <div class="social" style="top:154px"><i style="background:#29a9e1"></i>Short Posts</div>
  <div class="social" style="top:188px"><i style="background:#0e76a8"></i>Pro Network</div>
  <div class="social" style="top:222px"><i style="background:#d9302a"></i>Circles</div>
</footer>

<div class="copyright abs">Copyright © 2017 Harbor Logistics.&nbsp; All Rights Reserved.</div>

</body>
</html>
```